PLUME study results infographic

We enjoyed the previous infographic design you provided for us (The GLaRN cohort study Infographic), and would like to invite you to design another infographic in a similar style and layout.
We need an infographic which presents the results from the PLUME research trial. It should be colourful and engaging, in understandable language and showing the steps to get to the results. This is to showcase the results to patients/the public/clinicians, giving a brief summary of what the study proved. The final design should have the PLUME logo at the top (please see attached and https://plume.vextru.qb.zz.example/welcome-plume-trial)
I have attached the required logos which need to be used (PLUME, Carrowby Injury and Acute Care, University of Carrowby) as well as an example from another study, The GLaRN cohort study Infographic, as an example of what the layout could look like. Please DO NOT use the content from the The GLaRN cohort study Infographic example though, please instead use the content from the attached document 'PLUME_InfographicDesignInformation_PitchHive'.

```html
<!DOCTYPE html>
<html lang="en">
<head>
<meta charset="utf-8">
<title>PLUME Feasibility Trial Results</title>
<link href="https://fonts.googleapis.com/css2?family=Montserrat:ital,wght@0,400;0,500;0,600;0,700;0,800;1,700&display=swap" rel="stylesheet">
<style>
  :root {
    --backdrop: #169c98;
    --navy: #213862;
    --blue: #29abe2;
    --teal: #179a96;
    --band-light: #dbe9f8;
    --band-pale: #eef5fc;
    --panel: #b5d8f3;
    --grey: #8a8d91;
    --white: #ffffff;
  }
  * { margin: 0; padding: 0; box-sizing: border-box; }
  html, body { width: 913px; height: 1200px; overflow: hidden; }
  body {
    background: var(--backdrop);
    font-family: "Montserrat", Arial, sans-serif;
    color: var(--navy);
  }
  .poster {
    position: absolute; left: 92px; top: 84px;
    width: 729px; height: 1031px;
    background: var(--white); overflow: hidden;
  }
  .abs { position: absolute; }

  /* header */
  .header-shape { position: absolute; left: 0; top: 0; width: 729px; height: 240px; }
  .brand {
    left: 49px; top: 48px; display: flex; align-items: center; gap: 8px;
    color: var(--white); font-weight: 800; font-size: 30px; letter-spacing: 1px;
  }
  .brand-dot { width: 22px; height: 22px; border-radius: 50%; background: var(--blue); }
  .uni-box {
    left: 546px; top: 0; width: 89px; height: 114px; background: #1b2650;
    color: var(--white); display: flex; flex-direction: column; justify-content: flex-end;
    align-items: center; padding-bottom: 10px; text-align: center;
    font-size: 7px; font-weight: 500; letter-spacing: .5px; line-height: 1.3;
  }
  .uni-box strong { font-size: 11px; font-weight: 500; letter-spacing: .3px; }
  .trial-name { left: 0; width: 729px; top: 131px; text-align: center; color: var(--white); font-size: 18px; font-weight: 500; }
  .headline {
    left: 0; width: 729px; top: 155px; text-align: center; color: var(--blue);
    font-size: 21.5px; font-weight: 800; line-height: 26px; letter-spacing: -.3px;
  }

  .label {
    position: absolute; background: var(--teal); color: var(--white);
    font-weight: 700; font-size: 14px; height: 21px; line-height: 21px;
    padding: 0 7px; border-radius: 3px;
  }

  /* background */
  .bg-bar { left: 49px; top: 272px; width: 5px; height: 66px; background: var(--blue); }
  .bg-text { left: 65px; top: 268px; width: 380px; font-size: 13px; line-height: 18.5px; }
  .bg-text b { font-weight: 700; }
  .illus-care {
    left: 494px; top: 212px; width: 182px; height: 139px; border-radius: 8px;
    background: linear-gradient(160deg, #d9ecf9, #9fc4e6);
  }

  /* methods */
  .methods-band { left: 0; top: 356px; width: 729px; height: 175px; background: var(--band-light); }
  .methods-panel { position: absolute; left: 0; top: 356px; width: 729px; height: 175px; }
  .stat-big { font-size: 43px; font-weight: 800; color: var(--blue); letter-spacing: -1px; line-height: 1; }
  .stat-title { font-size: 19px; font-weight: 700; line-height: 1.2; }
  .stat-sub { font-size: 13px; line-height: 16px; }
  .illus-hospital {
    left: 259px; top: 399px; width: 114px; height: 131px;
    background: linear-gradient(180deg, #bfe3f7, #d9d9dd);
  }
  .rand { left: 518px; top: 389px; font-size: 13px; line-height: 18.5px; }
  .rand h3 { font-size: 13px; font-weight: 700; }
  .rand ul { list-style: none; }
  .rand li::before { content: "•"; margin: 0 7px 0 2px; }
  .rand-rule { left: 518px; top: 455px; width: 162px; border-top: 1px dotted var(--navy); }

  /* results */
  .results-band { left: 0; top: 531px; width: 729px; height: 225px; background: var(--band-pale); }
  .col-head { top: 576px; font-size: 16px; font-weight: 400; letter-spacing: -.3px; }
  .col-head b { font-weight: 800; }
  .divider { top: 578px; height: 127px; border-left: 1px dotted #9cc0e2; }
  .pct { font-size: 30px; font-weight: 800; letter-spacing: -1px; line-height: 1; }
  .pct.blue { color: var(--blue); }
  .pct-name { font-size: 13px; }
  .overall {
    left: 534px; top: 605px; width: 106px; height: 106px; border-radius: 50%;
    background: var(--blue); color: var(--white); font-size: 30px; font-weight: 800;
    display: flex; align-items: center; justify-content: center; letter-spacing: -1px;
  }
  .feasible {
    left: 49px; top: 725px; width: 631px; height: 26px; border-radius: 4px;
    background: var(--teal); color: var(--white); text-align: center;
    font-weight: 700; font-size: 12.5px; line-height: 26px;
  }

  /* conclusion */
  .conclusion-box { left: 49px; top: 773px; width: 631px; height: 78px; background: var(--band-light); }
  .conclusion-text {
    left: 49px; top: 803px; width: 631px; text-align: center;
    font-style: italic; font-weight: 700; font-size: 13.5px; line-height: 18px;
  }

  /* footer */
  .partner {
    left: 0; width: 729px; top: 887px; display: flex; justify-content: center; align-items: center; gap: 9px;
    color: var(--grey); font-size: 20px; font-weight: 500; letter-spacing: .3px;
  }
  .partner-square { width: 20px; height: 20px; background: var(--grey); }
  .funders { left: 0; width: 729px; top: 925px; text-align: center; font-size: 11.5px; line-height: 18.5px; }
  .email {
    left: 229px; top: 988px; width: 270px; height: 34px; background: var(--navy);
    color: var(--white); font-size: 12.5px; text-align: center; line-height: 34px;
  }
  .foot-band { left: 0; top: 1022px; width: 729px; height: 9px; background: var(--navy); }
</style>
</head>
<body>
<main class="poster">

  <svg class="header-shape" viewBox="0 0 729 240" aria-hidden="true">
    <polygon points="0,0 729,0 729,196 364,234 0,196" fill="#213862"/>
    <polygon points="0,196 364,234 729,196 729,202 364,240 0,202" fill="#29abe2"/>
  </svg>
  <div class="abs brand"><span class="brand-dot"></span>PLUME</div>
  <div class="abs uni-box">UNIVERSITY OF<strong>CARROWBY</strong></div>
  <p class="abs trial-name">The PLUME Feasibility Randomised Controlled Trial</p>
  <h1 class="abs headline">HIP FRACTURE SURGERY: CAN ‘VACUUM’ DRESSINGS<br>REDUCE DEEP INFECTIONS?</h1>

  <span class="label" style="left:49px;top:234px;">Background</span>
  <div class="abs bg-bar"></div>
  <p class="abs bg-text"><b>Adults &gt;65</b> years undergoing <b>hip fracture surgery</b> often develop surgical site infections (SSI). This study tested whether negative-pressure <b>‘vacuum’</b> dressings (iNPWT) could reduce infections compared to standard dressings.</p>
  <div class="abs illus-care" role="img" aria-label="Illustration of a carer pushing an older woman in a wheelchair"></div>

  <div class="abs methods-band"></div>
  <svg class="methods-panel" viewBox="0 0 729 175" aria-hidden="true">
    <polygon points="465,0 729,0 729,175 465,175 506,87" fill="#b5d8f3"/>
  </svg>
  <span class="label" style="left:49px;top:371px;">Methods</span>

  <svg class="abs" style="left:49px;top:413px;" width="92" height="92" viewBox="0 0 92 92" aria-hidden="true">
    <g fill="#29abe2">
      <circle cx="12" cy="30" r="6"/><rect x="2" y="38" width="18" height="50" rx="6"/>
      <circle cx="80" cy="30" r="6"/><rect x="72" y="38" width="18" height="50" rx="6"/>
      <circle cx="24" cy="18" r="7"/><rect x="13" y="27" width="22" height="61" rx="7"/>
      <circle cx="68" cy="18" r="7"/><rect x="57" y="27" width="22" height="61" rx="7"/>
      <circle cx="46" cy="9" r="9"/>
    </g>
    <rect x="31" y="20" width="30" height="70" rx="8" fill="#29abe2" stroke="#dbe9f8" stroke-width="2"/>
  </svg>
  <div class="abs" style="left:150px;top:409px;">
    <div class="stat-big">462</div>
    <div class="stat-title" style="margin-top:3px;">Patients</div>
    <div class="stat-sub">Randomised<br>62% of eligible</div>
  </div>

  <div class="abs illus-hospital" role="img" aria-label="Illustration of a hospital building with trees"></div>
  <div class="abs" style="left:364px;top:409px;">
    <div class="stat-big">05</div>
    <div class="stat-title" style="margin-top:3px;">Centres in UK</div>
    <div class="stat-sub">(2017–2018)</div>
  </div>

  <div class="abs rand">
    <h3>Randomised to</h3>
    <ul><li>Standard dressing</li><li>iNPWT vacuum dressing</li></ul>
  </div>
  <div class="abs rand-rule"></div>
  <div class="abs rand" style="top:467px;">
    <h3>Follow-up</h3>
    <p>30, 90 &amp; 120 days</p>
  </div>

  <div class="abs results-band"></div>
  <span class="label" style="left:49px;top:544px;">Results</span>

  <h2 class="abs col-head" style="left:49px;">Deep SSI at <b>30 days</b></h2>
  <h2 class="abs col-head" style="left:280px;">Deep SSI at <b>90 days</b></h2>
  <h2 class="abs col-head" style="left:495px;">Overall <b>30-day SSI rate</b></h2>
  <div class="abs divider" style="left:247px;"></div>
  <div class="abs divider" style="left:472px;"></div>

  <svg class="abs" style="left:49px;top:617px;" width="190" height="90" viewBox="0 0 190 90" aria-hidden="true">
    <circle cx="36" cy="48" r="26" fill="none" stroke="#213862" stroke-width="19"/>
    <circle cx="36" cy="48" r="26" fill="none" stroke="#29abe2" stroke-width="19" stroke-dasharray="37.6 200" transform="rotate(-90 36 48)"/>
    <circle cx="36" cy="48" r="16" fill="#fff"/>
    <rect x="28" y="41" width="16" height="14" rx="2" fill="none" stroke="#213862" stroke-width="1.5"/>
    <line x1="28" y1="45" x2="44" y2="45" stroke="#213862" stroke-width="1.5"/>
    <path d="M31 48h2M35 48h2M39 48h2M31 51h2M35 51h2M39 51h2" stroke="#213862" stroke-width="1.5"/>
    <path d="M36 14V6H94" fill="none" stroke="#29abe2" stroke-dasharray="2 2"/>
    <path d="M74 73H96" fill="none" stroke="#213862" stroke-dasharray="2 2"/>
  </svg>
  <div class="abs" style="left:146px;top:620px;"><div class="pct blue">1.9%</div><div class="pct-name">iNPWT</div></div>
  <div class="abs" style="left:146px;top:676px;"><div class="pct">6.4%</div><div class="pct-name">Standard</div></div>

  <svg class="abs" style="left:272px;top:617px;" width="190" height="90" viewBox="0 0 190 90" aria-hidden="true">
    <circle cx="36" cy="48" r="26" fill="none" stroke="#213862" stroke-width="19"/>
    <circle cx="36" cy="48" r="26" fill="none" stroke="#29abe2" stroke-width="19" stroke-dasharray="43 200" transform="rotate(-90 36 48)"/>
    <circle cx="36" cy="48" r="16" fill="#fff"/>
    <rect x="28" y="41" width="16" height="14" rx="2" fill="none" stroke="#213862" stroke-width="1.5"/>
    <line x1="28" y1="45" x2="44" y2="45" stroke="#213862" stroke-width="1.5"/>
    <path d="M31 48h2M35 48h2M39 48h2M31 51h2M35 51h2M39 51h2" stroke="#213862" stroke-width="1.5"/>
    <path d="M36 14V6H94" fill="none" stroke="#29abe2" stroke-dasharray="2 2"/>
    <path d="M74 73H96" fill="none" stroke="#213862" stroke-dasharray="2 2"/>
  </svg>
  <div class="abs" style="left:369px;top:620px;"><div class="pct blue">2.3%</div><div class="pct-name">iNPWT</div></div>
  <div class="abs" style="left:369px;top:676px;"><div class="pct">6.4%</div><div class="pct-name">Standard</div></div>

  <div class="abs overall">4.2%</div>

  <p class="abs feasible">Feasibility confirmed for a fully powered effectiveness trial.</p>

  <div class="abs conclusion-box"></div>
  <span class="label" style="left:49px;top:773px;">Conclusion</span>
  <p class="abs conclusion-text">The study showed a larger trial is feasible. Signals suggest vacuum dressings<br>may reduce infections, but further research is required.</p>

  <div class="abs partner"><span class="partner-square"></span>CARROWBY INJURY &amp; ACUTE CARE</div>
  <p class="abs funders">Royal Guild of Surgeons of Westmarch/Fenwick Health Trust (training fellowship),<br>Carrowby Clinical Research Centre (infrastructure support), Alder &amp; Vance (device supply).</p>

  <div class="abs email">r.halden@injury.carrowby.example</div>
  <div class="abs foot-band"></div>
</main>
</body>
</html>
```